Postcard Design

We are an upscale, full service real estate boutique based in Mt. Pleasant, SC. We will be having a Grand Opening of our beautiful, new office complete with high end custom home architecture and design. I will attach photos for your review. I would like to come up with a medium postcard to be mailed to clientele of Mt. Pleasant. Home prices between $300,000 - $2.2 million. The customers can call our office for the Grand Opening Listing Promotion or stop by our grand opening. We will have drawings for door prizes that include services at Brambleton Day Spa, Copper Kettle gift certificates, and they can register to win a cruise with a listing presentation. Our Grand Opening will be a couple of different dates, April 7, 2016 and April 21, 2016. I will want an order that lists the 7th and another order that will list the 21. The look should have a very "relaxing, beach" feel, but not Myrtle Beach...should reflect colors of the ocean, like you are on vacation. I will include logos and pics for your review. Thank you!

```html
<!DOCTYPE html>
<html lang="en">
<head>
<meta charset="utf-8">
<title>Harborleaf Real Estate – Grand Opening Postcard</title>
<link rel="stylesheet" href="https://fonts.googleapis.com/css2?family=Oswald:wght@400;500;600&family=Open+Sans:wght@400;600&family=Courgette&display=swap">
<style>
  :root {
    --ocean-deep: #0d4f95;
    --ocean-mid: #1f6fbf;
    --ocean-light: #2cb5e4;
    --aqua: #3fc8ea;
    --sand: #e9e3d6;
    --paper: #ffffff;
    --ink: #1a1a1a;
    --mute: #555b63;
    --silver: #c9cdd2;
    --backdrop: #e8ebef;
  }
  * { box-sizing: border-box; margin: 0; padding: 0; }
  html, body { width: 900px; height: 1200px; overflow: hidden; }
  body { background: var(--backdrop); position: relative; font-family: "Open Sans", sans-serif; }

  .postcard {
    position: absolute; left: 112px; width: 648px; height: 500px;
    background: var(--paper); overflow: hidden;
    box-shadow: 0 6px 18px rgba(0,0,0,.25);
  }
  .postcard--front { top: 52px; }
  .postcard--back { top: 645px; }
  .postcard svg.artwork { position: absolute; inset: 0; }

  /* front */
  .headline {
    position: absolute; left: 304px; top: 20px; width: 322px; text-align: center; color: var(--paper);
  }
  .headline__title { font-family: "Oswald", sans-serif; font-weight: 500; font-size: 29px; letter-spacing: -0.3px; line-height: 1.2; white-space: nowrap; }
  .headline__title span { color: var(--aqua); }
  .headline__script { font-family: "Courgette", cursive; font-size: 25px; line-height: 1.15; white-space: nowrap; }
  .headline__sub { font-size: 16px; line-height: 1.2; white-space: nowrap; }
  .headline__rule { height: 2px; background: var(--paper); margin: 6px 6px 8px; }
  .headline__dates { font-family: "Oswald", sans-serif; font-size: 23px; display: flex; justify-content: space-between; padding: 0 6px; white-space: nowrap; }

  .price-badge {
    position: absolute; left: 174px; top: 220px; width: 128px; text-align: center; color: var(--paper);
  }
  .price-badge__label { font-family: "Oswald", sans-serif; font-size: 17px; line-height: 1.1; }
  .price-badge__main { font-family: "Oswald", sans-serif; font-weight: 600; font-size: 30px; color: var(--ink); line-height: 1.15; }
  .price-badge__range { font-family: "Oswald", sans-serif; font-size: 12.5px; white-space: nowrap; }

  .brand { position: absolute; text-align: center; color: var(--ocean-light); font-family: "Open Sans", sans-serif; font-weight: 600; }
  .brand__mark { display: block; margin: 0 auto 6px; border-radius: 50%; border: 3px solid var(--ocean-light); }
  .brand--front { left: 20px; top: 378px; width: 170px; }
  .brand--front .brand__mark { width: 46px; height: 46px; }
  .brand--front .brand__name { font-size: 21px; letter-spacing: 1.5px; line-height: 1.1; }
  .brand--front .brand__tag { font-size: 9.5px; letter-spacing: 2.5px; }
  .brand--back { left: 316px; top: 18px; width: 100px; }
  .brand--back .brand__mark { width: 28px; height: 28px; border-width: 2px; margin-bottom: 4px; }
  .brand--back .brand__name { font-size: 13px; letter-spacing: 1px; line-height: 1.1; }
  .brand--back .brand__tag { font-size: 6px; letter-spacing: 1.5px; }

  /* back */
  .about { position: absolute; left: 18px; top: 150px; width: 226px; color: var(--paper); text-align: center; }
  .pill {
    display: inline-block; background: linear-gradient(#ffffff, #cfd3d8); color: var(--ink);
    font-family: "Oswald", sans-serif; font-weight: 500; font-size: 13px;
    padding: 1px 12px; border-radius: 10px;
  }
  .about__text { margin-top: 6px; font-size: 11.2px; line-height: 14.6px; text-align: justify; }
  .contact { position: absolute; left: 18px; top: 296px; width: 226px; text-align: center; }
  .contact .pill { border-radius: 2px; background: linear-gradient(#b9bdc2, #8d9298); padding: 2px 16px; font-size: 13.5px; }
  .contact__phone { font-family: "Oswald", sans-serif; font-weight: 500; font-size: 21px; color: var(--ocean-mid); margin-top: 4px; line-height: 1.3; }
  .contact__address { font-size: 11.5px; color: var(--mute); line-height: 15px; margin-top: 2px; }
  .contact__pin { display: inline-block; width: 8px; height: 11px; vertical-align: -1px; margin-right: 3px; }

  .stamp-box { position: absolute; left: 519px; top: 48px; width: 80px; height: 80px; border: 1.5px solid #333; }
  .address-line { position: absolute; left: 351px; width: 243px; height: 1.5px; background: #444; }
</style>
</head>
<body>

<section class="postcard postcard--front" aria-label="Postcard front">
  <svg class="artwork" width="648" height="500" viewBox="0 0 648 500">
    <defs>
      <linearGradient id="oceanPanel" x1="0" y1="0" x2="1" y2="1">
        <stop offset="0" stop-color="#1d78c8"/>
        <stop offset="1" stop-color="#0c3f7e"/>
      </linearGradient>
      <linearGradient id="beachScene" x1="0" y1="0" x2="0" y2="1">
        <stop offset="0" stop-color="#2f6fb0"/>
        <stop offset=".35" stop-color="#7fc9e0"/>
        <stop offset=".55" stop-color="#49c3c6"/>
        <stop offset=".75" stop-color="#e8e2d4"/>
        <stop offset="1" stop-color="#f3efe7"/>
      </linearGradient>
      <linearGradient id="houseScene" x1="0" y1="0" x2="0" y2="1">
        <stop offset="0" stop-color="#8fb8dc"/>
        <stop offset=".45" stop-color="#b9c9d8"/>
        <stop offset=".8" stop-color="#7b8d6a"/>
        <stop offset="1" stop-color="#b7b3a8"/>
      </linearGradient>
      <radialGradient id="badgeFill" cx=".5" cy=".4" r=".6">
        <stop offset="0" stop-color="#49c8ef"/>
        <stop offset="1" stop-color="#1899cf"/>
      </radialGradient>
      <linearGradient id="silverRing" x1="0" y1="0" x2="1" y2="1">
        <stop offset="0" stop-color="#ffffff"/>
        <stop offset="1" stop-color="#9ba2aa"/>
      </linearGradient>
    </defs>
    <rect x="190" y="0" width="458" height="500" fill="url(#oceanPanel)"/>
    <path role="img" aria-label="Photo of a light blue two-storey coastal home with shutters among trees"
          d="M0,0 H295 C250,70 238,200 290,300 C230,330 120,345 0,338 Z" fill="url(#houseScene)"/>
    <path d="M0,338 C120,345 230,330 290,300 C260,380 220,450 210,500 H0 Z" fill="#ffffff"/>
    <path d="M290,300 C260,380 220,450 210,500" fill="none" stroke="var(--ocean-light)" stroke-width="8"/>
    <path d="M295,0 C250,70 238,200 290,300" fill="none" stroke="#ffffff" stroke-width="5"/>
    <path d="M305,0 C262,70 250,200 300,300" fill="none" stroke="var(--ocean-light)" stroke-width="3"/>
    <path role="img" aria-label="Photo of a smiling couple walking hand in hand on a white sand beach by turquoise water"
          d="M215,500 C228,380 300,228 420,198 C520,176 600,190 648,215 V500 Z" fill="url(#beachScene)"/>
    <path d="M300,235 C370,180 520,160 648,212" fill="none" stroke="var(--aqua)" stroke-width="10"/>
    <path d="M300,244 C370,192 520,172 648,222" fill="none" stroke="#ffffff" stroke-width="3"/>
    <circle cx="238" cy="278" r="80" fill="url(#silverRing)"/>
    <circle cx="238" cy="278" r="68" fill="url(#badgeFill)"/>
  </svg>

  <header class="headline">
    <h1 class="headline__title">EXPERIENCE THE <span>DIFFERENCE</span></h1>
    <p class="headline__script">Our Grand Opening</p>
    <p class="headline__sub">will be a couple of different dates</p>
    <div class="headline__rule"></div>
    <p class="headline__dates"><span>April 7, 2016</span><span>|</span><span>April 21, 2016</span></p>
  </header>

  <div class="price-badge">
    <p class="price-badge__label">Home Prices</p>
    <p class="price-badge__main">Between</p>
    <p class="price-badge__range">$300,000 - $2.2 million</p>
  </div>

  <div class="brand brand--front">
    <span class="brand__mark"></span>
    <p class="brand__name">HARBORLEAF</p>
    <p class="brand__tag">REAL ESTATE</p>
  </div>
</section>

<section class="postcard postcard--back" aria-label="Postcard back">
  <svg class="artwork" width="648" height="500" viewBox="0 0 648 500">
    <defs>
      <linearGradient id="backPanel" x1="0" y1="0" x2="0" y2="1">
        <stop offset="0" stop-color="#1f6fbf"/>
        <stop offset="1" stop-color="#0d4f95"/>
      </linearGradient>
      <linearGradient id="hammockScene" x1="0" y1="0" x2="0" y2="1">
        <stop offset="0" stop-color="#5c8fb8"/>
        <stop offset=".5" stop-color="#c9c1b2"/>
        <stop offset="1" stop-color="#e4ddd0"/>
      </linearGradient>
      <linearGradient id="contactFade" x1="0" y1="0" x2="0" y2="1">
        <stop offset="0" stop-color="#ffffff"/>
        <stop offset="1" stop-color="#c6cacf"/>
      </linearGradient>
    </defs>
    <path d="M0,0 H292 C255,90 250,200 262,250 C272,300 270,360 305,412 H0 Z" fill="url(#backPanel)"/>
    <path role="img" aria-label="Photo of a relaxed couple sitting together in a rope hammock on the beach"
          d="M0,0 H292 C282,60 270,110 240,130 C160,150 60,145 0,132 Z" fill="url(#hammockScene)"/>
    <path d="M0,132 C60,145 160,150 240,130 C270,110 282,60 292,0" fill="none" stroke="var(--aqua)" stroke-width="4"/>
    <path d="M0,284 C90,302 200,298 268,284 C272,330 282,375 305,412 H0 Z" fill="url(#contactFade)"/>
    <path d="M0,284 C90,302 200,298 268,284" fill="none" stroke="var(--ocean-light)" stroke-width="3"/>
    <path d="M294,0 C257,90 252,200 264,250 C274,300 275,360 308,412" fill="none" stroke="var(--ocean-light)" stroke-width="3"/>
  </svg>

  <div class="about">
    <span class="pill">About Us</span>
    <p class="about__text">Harborleaf Real Estate is a full service real estate company that specializes in high-end customer service from the moment we answer your call or email. When you step into the Harborleaf way, get ready to experience the difference as we rally our team around you!</p>
  </div>

  <div class="contact">
    <span class="pill">Call Today</span>
    <p class="contact__phone">843-555-0147</p>
    <p class="contact__address"><svg class="contact__pin" viewBox="0 0 8 11" aria-hidden="true"><path d="M0,4 a4,4 0 1 1 8,0 c0,3 -4,7 -4,7 s-4,-4 -4,-7 z" fill="#1f6fbf"/><circle cx="4" cy="4" r="1.5" fill="#fff"/></svg>1260 Shoreline<br>Drive Mount Pleasant, SC 29464</p>
  </div>

  <div class="brand brand--back">
    <span class="brand__mark"></span>
    <p class="brand__name">HARBORLEAF</p>
    <p class="brand__tag">REAL ESTATE</p>
  </div>

  <div class="stamp-box" aria-label="Stamp area"></div>
  <div class="address-line" style="top:263px"></div>
  <div class="address-line" style="top:296px"></div>
  <div class="address-line" style="top:330px"></div>
</section>

</body>
</html>
```